CBD Banner Ad for Print and Zentrix

I we would like a modern European chic that we can use in a 1/4 page ad in our local magazine and also use as our banner ad in the Zentrix ad searches. <br/><br/>We are a high end CBD boutique shop that has their own brand as well as a carefully curated selection of the top end CBD products out on the market. The final design should promote the health and well being that we are trying to live ourselves. We DO NOT want the use of marijuana paraphernalia or like substances. Think Yoga Studio meets Morvik inside of a health store. <br/><br/>Use any images you would like...I have attached a sample product render as well as the inside of our store...but take this in the direction you would like.<br/><br/>The winner will have the added bonus of being able to create 10 more ads for us in the next 6 months.

Target Market(s)

Our target market are the middle to upperclass professional workers that want to take CBD but were afraid due to misinformation or stigma

Font styles to use
Sans Serif

Colors
33b8a4
86cfc6
0792cd
3277b5
85acd3

Requirements
Must have
• A good clean modern design.
• Natural. Organic. Crisp. Welcoming.
Nice to have
• Opal Meadow
• CBD for wellness. CBD for life.
• The font we use for the rest of our campaigns is Adam.
Should not have
• Absolutely NO marijuana leaves, paraphernalia, or references. We are working hard to educate people and get rid of the stigma.

```html
<!DOCTYPE html>
<html lang="en">
<head>
<meta charset="utf-8">
<title>Opal Meadow — CBD for Wellness</title>
<link href="https://fonts.googleapis.com/css2?family=Raleway:wght@200;300;400&display=swap" rel="stylesheet">
<style>
  :root {
    --canvas-white: #ffffff;
    --scene-blue: #6b98bb;
    --sand: #efe6d4;
    --sand-shade: #e9e2d3;
    --contour: #dbe6e0;
    --teal-deep: #6dd1cb;
    --teal-soft: #89cfc5;
    --ocean: #0792cd;
    --sky: #85acd3;
    --clay: #e6a68b;
    --ink: #2b2b2b;
    --title-white: #ffffff;
    --frame-line: #555555;
  }
  * { margin: 0; padding: 0; box-sizing: border-box; }
  html, body {
    width: 1200px;
    height: 2380px;
    overflow: hidden;
    background: var(--canvas-white);
    font-family: "Raleway", sans-serif;
  }
  .canvas {
    position: relative;
    width: 1200px;
    height: 2380px;
  }
  .print-zone {
    position: absolute;
    left: 0; top: 0;
    width: 1200px; height: 1194px;
    background: var(--canvas-white);
  }
  .showcase-zone {
    position: absolute;
    left: 0; top: 1194px;
    width: 1200px; height: 1186px;
    background: var(--scene-blue);
  }
  .ad-card {
    position: absolute;
    width: 674px;
    height: 872px;
    overflow: hidden;
    background: var(--sand);
    transform-origin: top left;
  }
  .ad-card--framed {
    left: 263px; top: 139px;
    outline: 1px solid var(--frame-line);
  }
  .ad-card--display {
    left: 330px; top: 244px;
    transform: scale(0.8);
    box-shadow: 0 20px 40px rgba(30, 60, 90, 0.35);
  }
  .contour-field {
    position: absolute;
    inset: 0;
    background:
      radial-gradient(ellipse 60% 40% at 30% 45%, var(--contour) 0%, transparent 70%),
      radial-gradient(ellipse 50% 60% at 80% 70%, var(--contour) 0%, transparent 70%),
      linear-gradient(160deg, var(--sand) 0%, var(--sand-shade) 50%, var(--sand) 100%);
  }
  .shapes {
    position: absolute;
    inset: 0;
    width: 674px;
    height: 872px;
  }
  .brand-title {
    position: absolute;
    left: 150px;
    top: 108px;
    color: var(--title-white);
    font-weight: 200;
    font-size: 58px;
    line-height: 80px;
    letter-spacing: 0.4em;
    text-transform: uppercase;
    white-space: nowrap;
  }
  .brand-title span { display: block; }
  .tagline {
    position: absolute;
    left: 152px;
    top: 566px;
    color: var(--ink);
    font-weight: 400;
    font-size: 21px;
    line-height: 26px;
    letter-spacing: 0.05em;
    word-spacing: 0.2em;
  }
  .tagline span { display: block; }
  .web-line {
    position: absolute;
    left: 31px;
    top: 789px;
    display: flex;
    align-items: center;
    gap: 10px;
    color: var(--ink);
    font-weight: 300;
    font-size: 23px;
  }
  .web-dot {
    width: 15px; height: 15px;
    border-radius: 50%;
    background: var(--ink);
  }
</style>
</head>
<body>
<main class="canvas">

  <section class="print-zone">
    <article class="ad-card ad-card--framed">
      <div class="contour-field" role="img" aria-label="Faint pale-teal topographic contour line pattern on sand background"></div>
      <svg class="shapes" viewBox="0 0 674 872" aria-hidden="true">
        <circle cx="40" cy="20" r="120" fill="var(--teal-deep)"/>
        <path d="M160 88 C178 80 190 96 182 118 C176 138 168 150 148 154 C126 158 112 146 118 128 C124 112 142 96 160 88 Z" fill="var(--ocean)"/>
        <circle cx="474" cy="593" r="42" fill="var(--sky)"/>
        <path d="M512 740 C528 752 520 774 500 790 C486 802 482 820 464 826 C444 832 436 810 442 790 C450 764 488 726 512 740 Z" fill="var(--clay)"/>
        <circle cx="640" cy="912" r="162" fill="var(--teal-soft)"/>
      </svg>
      <h1 class="brand-title"><span>Opal</span><span>Meadow</span></h1>
      <p class="tagline"><span>CBD FOR WELLNESS</span><span>CBD FOR LIFE</span></p>
      <p class="web-line"><span class="web-dot"></span>opalmeadow.life</p>
    </article>
  </section>

  <section class="showcase-zone">
    <article class="ad-card ad-card--display">
      <div class="contour-field" role="img" aria-label="Faint pale-teal topographic contour line pattern on sand background"></div>
      <svg class="shapes" viewBox="0 0 674 872" aria-hidden="true">
        <circle cx="40" cy="20" r="120" fill="var(--teal-deep)"/>
        <path d="M160 88 C178 80 190 96 182 118 C176 138 168 150 148 154 C126 158 112 146 118 128 C124 112 142 96 160 88 Z" fill="var(--ocean)"/>
        <circle cx="474" cy="593" r="42" fill="var(--sky)"/>
        <path d="M512 740 C528 752 520 774 500 790 C486 802 482 820 464 826 C444 832 436 810 442 790 C450 764 488 726 512 740 Z" fill="var(--clay)"/>
        <circle cx="640" cy="912" r="162" fill="var(--teal-soft)"/>
      </svg>
      <h2 class="brand-title"><span>Opal</span><span>Meadow</span></h2>
      <p class="tagline"><span>CBD FOR WELLNESS</span><span>CBD FOR LIFE</span></p>
      <p class="web-line"><span class="web-dot"></span>opalmeadow.life</p>
    </article>
  </section>

</main>
</body>
</html>
```